Business card design for Bront Engineering Qavo

We need a new business card design along with all the necessary to place an order. The company is Bront Engineering Qavo and we recently updated our logo.

```html
<!DOCTYPE html>
<html lang="en">
<head>
<meta charset="utf-8">
<title>Bront Engineering Qavo — Business Card</title>
<link rel="stylesheet" href="https://fonts.googleapis.com/css2?family=Montserrat:wght@400;500;600;700&display=swap">
<style>
  :root {
    --backdrop: #1c1c20;
    --card: #222426;
    --card-edge: #2b2d30;
    --silver: #a9a9ab;
    --silver-light: #cfcfd1;
    --muted: #8e8f92;
    --accent: #e6c125;
  }
  * { box-sizing: border-box; margin: 0; padding: 0; }
  html, body {
    width: 1200px;
    height: 800px;
    overflow: hidden;
    background: var(--backdrop);
    font-family: "Montserrat", Arial, sans-serif;
  }
  .canvas {
    width: 1200px;
    height: 800px;
    display: flex;
    align-items: center;
    justify-content: center;
    gap: 40px;
  }
  .card {
    width: 540px;
    height: 310px;
    border-radius: 22px;
    background: var(--card);
    box-shadow: inset 0 0 0 1px var(--card-edge), 0 18px 40px rgba(0,0,0,.45);
    position: relative;
    overflow: hidden;
  }
  /* Front side */
  .card--front {
    display: flex;
    align-items: center;
    justify-content: center;
  }
  .wordmark {
    display: flex;
    align-items: center;
    gap: 10px;
  }
  .wordmark__square {
    width: 12px;
    height: 12px;
    background: var(--silver);
  }
  .wordmark__name {
    font-weight: 600;
    font-size: 22px;
    letter-spacing: 0.08em;
    text-transform: uppercase;
    color: var(--silver);
  }
  /* Back side */
  .card--back {
    display: flex;
    align-items: center;
    padding: 0 34px;
  }
  .card--back .wordmark__square { background: var(--accent); width: 10px; height: 10px; }
  .card--back .wordmark__name {
    font-size: 15px;
    line-height: 1.35;
    width: 170px;
  }
  .divider {
    width: 1px;
    height: 120px;
    background: var(--accent);
    margin: 0 26px 0 22px;
    flex-shrink: 0;
  }
  .contact { color: var(--muted); font-size: 11.5px; line-height: 1.55; }
  .contact__name {
    font-weight: 700;
    font-size: 14px;
    letter-spacing: 0.04em;
    text-transform: uppercase;
    color: var(--silver-light);
  }
  .contact__role { color: var(--accent); font-weight: 500; font-size: 12px; margin-bottom: 12px; }
  .contact__address { margin-bottom: 12px; }
  .contact__line { display: flex; align-items: center; gap: 8px; }
  .contact__icon { width: 12px; height: 12px; flex-shrink: 0; }
</style>
</head>
<body>
<main class="canvas">
  <section class="card card--front" aria-label="Card front">
    <div class="wordmark">
      <span class="wordmark__square"></span>
      <span class="wordmark__name">Bront Engineering Qavo</span>
    </div>
  </section>

  <section class="card card--back" aria-label="Card back">
    <div class="wordmark">
      <span class="wordmark__square"></span>
      <span class="wordmark__name">Bront Engineering Qavo</span>
    </div>
    <span class="divider"></span>
    <div class="contact">
      <p class="contact__name">Dara M. Kelloway</p>
      <p class="contact__role">Partner</p>
      <p class="contact__address">Level 4, 88 Harbour Lane<br>Sydney NSW 2031</p>
      <p class="contact__line">
        <svg class="contact__icon" viewBox="0 0 12 12" aria-hidden="true">
          <rect x="1.5" y="1.5" width="9" height="9" rx="1" fill="none" stroke="var(--accent)" stroke-width="1.6"/>
        </svg>
        0123 987 604
      </p>
      <p class="contact__line">
        <svg class="contact__icon" viewBox="0 0 12 12" aria-hidden="true">
          <rect x="0.5" y="2" width="11" height="8" fill="var(--accent)"/>
          <path d="M0.5 2 L6 6.5 L11.5 2" fill="none" stroke="var(--card)" stroke-width="1.1"/>
        </svg>
        info@brontqavo.co
      </p>
    </div>
  </section>
</main>
</body>
</html>
```